Online radio: TunaWave homepage redesign

TunaWave is one of the world's leading brands of personalizable online radio -- similar to Melodex, but aimed at a somewhat older audience (age 35-54).

We'd like to redesign our homepage with a more contemporary look: It should emphasize our wide variety of GENRES (as the primary navigation), with the search field easy to find as a secondary navigation.

We'd like to retain our corporate color of maroon/plum. (We are not committed to the gold/yellow secondary color.)

See our current homepage at www.tunawave-example.com and our in-house attempt at an improved design at http://web4.tunawave-example.com/finder/2013ms/.

Ideally, we'd like to see designs for up to THREE different states:

(1) An initial state when users first come to the page.

(2) What the page would look like as the user is looking at channel options.

(3) What the page would look like once the media player is launched.

However, you may be able to combine (2) and (3) in a single screenshot.

Thanks!
Updates

At the request of several designers, we have decided to extend our deadline by four days. At the same time, we have increased our budget, including the addition of a 2nd place award. Thanks for your excellent work!

Thanks very much for your designs! We are very pleased with the overall quality of the work we are seeing. One reminder: As our brief says, the user interface "should emphasize our wide variety of GENRES (as the primary navigation), with the search field easy to find as a secondary navigation," and we feel that your design uses the SEARCH field as the primary navigation. Many of the designs use a large search field as the primary navigation. If yours does, you might want to tweak your design to put a greater emphasis on browsing genres as the primary navigation. Thanks and good luck!

Target Market(s)

Adults age 35-54 listening to online radio at work

Industry/Entity Type

Radio

Font styles to use
Sans Serif

Requirements
Must have
• This is a design/UI project -- we do not need code

```html
<!DOCTYPE html>
<html lang="en">
<head>
<meta charset="utf-8">
<title>TunaWave — Online Radio</title>
<link href="https://fonts.googleapis.com/css2?family=Source+Sans+3:ital,wght@0,300;0,400;0,600;0,700;1,300&display=swap" rel="stylesheet">
<style>
:root{
  --plum:#5e0b4b;
  --plum-dark:#4a0839;
  --hero-dark:#3f3f42;
  --hero-mid:#5a5a5e;
  --page-bg:#ececec;
  --panel-bg:#f6f6f6;
  --btn-grey:#e6e6e6;
  --btn-line:#c9c9c9;
  --text-dark:#2a2a2a;
  --text-mid:#555;
  --footer-bg:#222222;
  --white:#ffffff;
}
*{box-sizing:border-box;margin:0;padding:0}
html,body{width:952px;height:1200px;overflow:hidden}
body{position:relative;background:var(--page-bg);font-family:"Source Sans 3",Arial,sans-serif;color:var(--text-dark)}
.abs{position:absolute}

/* Hero */
.hero{left:0;top:0;width:952px;height:446px;background:linear-gradient(160deg,#4b4b4f 0%,#56565b 40%,#45454a 75%,#3b3b3f 100%)}
.hero-photo{left:0;top:0;width:952px;height:446px;background:radial-gradient(ellipse at 40% 30%,rgba(120,120,125,.45),transparent 55%),radial-gradient(ellipse at 70% 55%,rgba(40,70,110,.35),transparent 50%),radial-gradient(ellipse at 10% 60%,rgba(110,40,40,.3),transparent 45%)}
.brand{left:102px;top:20px;width:192px;height:48px;background:var(--plum);display:flex;align-items:center;gap:8px;padding-left:10px;color:var(--white);font-size:27px;font-weight:600;letter-spacing:-.5px}
.brand-dot{width:28px;height:28px;border-radius:50%;background:#f2d21a;flex:none}
.auth{top:14px;height:16px;font-size:9px;font-weight:700;color:var(--white);display:flex;align-items:center;justify-content:center}
.auth-login{left:759px;width:42px;background:var(--plum)}
.auth-signup{left:809px;width:43px;background:#9a9a9a}
.nav{top:62px;font-size:13px;font-weight:300;color:var(--white)}
.headline{left:0;top:188px;width:952px;text-align:center;color:var(--white);font-size:35px;font-weight:400}
.search{left:250px;top:302px;width:452px;height:62px;background:var(--white);border:2px solid #ddd;border-radius:4px;display:flex}
.search-field{flex:1;display:flex;align-items:center;padding-left:38px;font-size:17px;font-style:italic;font-weight:300;color:#999}
.search-btn{width:80px;border-left:1px solid #ccc;display:flex;align-items:center;justify-content:center}

/* Selectors */
.select{top:484px;height:38px;display:flex;font-size:18px}
.select-label{flex:1;display:flex;align-items:center;justify-content:center}
.select-arrow{width:56px;display:flex;align-items:center;justify-content:center}
.select-active{left:162px;width:181px;background:var(--plum);color:var(--white);border-radius:2px}
.select-active .select-label{padding-left:0}
.select-plain{width:180px;background:var(--btn-grey);border:1px solid #d8d8d8;color:#333}
.select-plain .select-arrow{border-left:1px solid var(--btn-line)}
.menu{left:162px;top:530px;width:181px;background:var(--btn-grey);border:1px solid #ccc;border-radius:2px}
.menu-notch{left:298px;top:524px;width:12px;height:12px;background:var(--btn-grey);border-left:1px solid #ccc;border-top:1px solid #ccc;transform:rotate(45deg)}
.menu-item{height:35px;display:flex;align-items:center;padding-left:14px;font-size:11.5px;color:var(--text-mid);border-bottom:1px solid #d0d0d0}
.menu-item:last-child{border-bottom:none}
.menu-item.is-hover{color:var(--plum);font-weight:600}

/* Genre grid */
.grid-panel{left:182px;top:656px;width:586px;height:230px;background:var(--panel-bg)}
.genre{width:154px;text-align:center}
.covers{display:flex;gap:1px;height:50px}
.cover{flex:1}
.genre-name{margin-top:10px;font-size:18px;color:var(--text-dark)}
.load-more{left:398px;top:902px;width:157px;height:50px;background:var(--plum);color:var(--white);font-size:17px;font-weight:600;display:flex;align-items:center;justify-content:center;border-radius:2px}

/* Footer */
.footer{left:0;top:1032px;width:952px;height:168px;background:var(--footer-bg);color:var(--white)}
.footer-title{left:122px;top:16px;font-size:17px;font-weight:600}
.footer-links{left:122px;top:50px;width:680px;font-size:13px;line-height:16px}
.copyright{left:124px;top:142px;font-size:9px}
.socials{left:702px;top:140px;display:flex;gap:7px}
.social{width:19px;height:19px;border-radius:50%;background:#000}
</style>
</head>
<body>

<header>
  <div class="abs hero"></div>
  <div class="abs hero-photo" role="img" aria-label="Background photo of a listener wearing headphones over splattered paint textures"></div>
  <div class="abs brand"><span class="brand-dot"></span>TunaWave</div>
  <a class="abs auth auth-login">Log In</a>
  <a class="abs auth auth-signup">Sign Up</a>
  <nav>
    <span class="abs nav" style="left:593px">Home</span>
    <span class="abs nav" style="left:650px">About &amp; Contact</span>
    <span class="abs nav" style="left:765px">Help</span>
    <span class="abs nav" style="left:815px">Mobile</span>
  </nav>
  <h1 class="abs headline">Thousands of radio stations with endless music</h1>
  <div class="abs search">
    <div class="search-field">Search by artist or keyword</div>
    <div class="search-btn">
      <svg width="34" height="30" viewBox="0 0 34 30"><circle cx="12" cy="12" r="9" fill="none" stroke="#5e0b4b" stroke-width="3.5"/><line x1="19" y1="18" x2="30" y2="27" stroke="#5e0b4b" stroke-width="4.5" stroke-linecap="round"/></svg>
    </div>
  </div>
</header>

<main>
  <div class="abs select select-active">
    <div class="select-label" style="padding-left:12px">DJ Picks</div>
    <div class="select-arrow"><svg width="18" height="14" viewBox="0 0 18 14"><path d="M0 0H18L9 14Z" fill="#fff"/></svg></div>
  </div>
  <div class="abs select select-plain" style="left:386px">
    <div class="select-label">Genres</div>
    <div class="select-arrow"><svg width="18" height="14" viewBox="0 0 18 14"><path d="M0 0H18L9 14Z" fill="#222"/></svg></div>
  </div>
  <div class="abs select select-plain" style="left:610px">
    <div class="select-label">Surprise Me</div>
    <div class="select-arrow"><svg width="18" height="14" viewBox="0 0 18 14"><path d="M0 0H18L9 14Z" fill="#222"/></svg></div>
  </div>

  <div class="abs menu-notch"></div>
  <div class="abs menu">
    <div class="menu-item">Most Popular Channels</div>
    <div class="menu-item is-hover">Get Motivated</div>
    <div class="menu-item">Concentrate</div>
  </div>

  <div class="abs grid-panel"></div>

  <div class="abs genre" style="left:200px;top:670px">
    <div class="covers" role="img" aria-label="Album covers for Top 40 and pop hits">
      <span class="cover" style="background:#e8dc2a"></span><span class="cover" style="background:#8a6a4e"></span><span class="cover" style="background:#7a4a1c"></span>
    </div>
    <div class="genre-name">Top 40 / Pop Hits</div>
  </div>
  <div class="abs genre" style="left:392px;top:670px">
    <div class="covers" role="img" aria-label="Album covers for lite hits">
      <span class="cover" style="background:#9a6a5a"></span><span class="cover" style="background:#4f7a78"></span><span class="cover" style="background:#9aa3a8"></span>
    </div>
    <div class="genre-name">Lite Hits</div>
  </div>
  <div class="abs genre" style="left:584px;top:670px">
    <div class="covers" role="img" aria-label="Album covers for country">
      <span class="cover" style="background:#3a2e2c"></span><span class="cover" style="background:#cfcac4"></span><span class="cover" style="background:#3d4a2a"></span>
    </div>
    <div class="genre-name">Country</div>
  </div>
  <div class="abs genre" style="left:200px;top:774px">
    <div class="covers" role="img" aria-label="Album covers for classical">
      <span class="cover" style="background:#3a3330"></span><span class="cover" style="background:#5a3a2a"></span><span class="cover" style="background:#c9c0b8"></span>
    </div>
    <div class="genre-name">Classical</div>
  </div>
  <div class="abs genre" style="left:392px;top:774px">
    <div class="covers" role="img" aria-label="Album covers for classic rock">
      <span class="cover" style="background:#6a7a84"></span><span class="cover" style="background:#4a8aa4"></span><span class="cover" style="background:#b89a82"></span>
    </div>
    <div class="genre-name">Classic Rock</div>
  </div>
  <div class="abs genre" style="left:584px;top:774px">
    <div class="covers" role="img" aria-label="Album covers for smooth jazz">
      <span class="cover" style="background:#8a2a2a"></span><span class="cover" style="background:#dcdad6"></span><span class="cover" style="background:#3a3636"></span>
    </div>
    <div class="genre-name">Smooth Jazz</div>
  </div>

  <a class="abs load-more">Load more</a>
</main>

<footer class="abs footer">
  <h2 class="abs footer-title">QUICK LINKS</h2>
  <p class="abs footer-links">•My History •My Favorites •Most Popular •Workday Mood •Great Summer Music • Get Motivated • Concentrate •Almost 5 O'ClockRelax and Unwind •Adult • Alternative •Rock Adult •Contemporary• &nbsp;'50sDecade •'60sDecade • '70sDecade• '80sDecade • '90sDecade</p>
  <p class="abs copyright">©TunaWave2014. All Rights Resercved</p>
  <div class="abs socials">
    <span class="social"></span><span class="social"></span><span class="social"></span><span class="social"></span><span class="social"></span><span class="social"></span>
  </div>
</footer>

</body>
</html>
```